依頼詳細
緑丘台駅前にございますが、ビルの5階の為目立ちません。看板の設置場所添付しますので確認下さい。道路からは少ししか見えません。 注意):後ろ全面の壁の色がコンクリート色に変更となります。  看板へのイメージですが安心、親しみやすさ、元気、です。 当社のイメージカラーはオレンジです。
記載項目
サイズはW590×H900です。 電話番号はいりません。 必須は・賃貸専門・当社のロゴか社名どちらか(出来れば両方希望ですが一つでも可)・5階と分かる事・以上です。 一番は賃貸専門を目立たせて下さい。
希望イメージ
シンプル 複雑
単色 カラフル
暗い 明るい
日常 高級
遊び心 厳粛
未来的 伝統的
女性的 男性的
希望する色
納品ファイル
• 高解像度JPG (.jpg)
• イラストレーター形式 (.ai)
• フォトショップ形式 (.psd)
• PNG形式 (.png)
補足説明
■ 選んだ理由

一番イメージ通りのデザインでした。
シンプルで見やすく良かったです。

■ 提案者全員のお礼・コメント

皆様色々ご提案頂きまして誠に有難うございました。
どれも素晴くとても悩みました。
次回ご縁ございましたら宜しくお願い致します。

```html
<!DOCTYPE html>
<html lang="ja">
<head>
<meta charset="UTF-8">
<title>賃貸専門 サニーネスト 看板</title>
<link href="https://fonts.googleapis.com/css2?family=M+PLUS+Rounded+1c:wght@500;800;900&display=swap" rel="stylesheet">
<style>
  :root{
    --orange:#f28c12;
    --orange-deep:#e06a00;
    --orange-light:#ffb347;
    --orange-pale:#ffd28a;
    --white:#ffffff;
    --ink:#2a2a2a;
  }
  *{margin:0;padding:0;box-sizing:border-box}
  html,body{width:786px;height:1200px;overflow:hidden}
  body{font-family:"M PLUS Rounded 1c",sans-serif;background:var(--orange)}
  .signboard{
    position:relative;width:786px;height:1200px;overflow:hidden;
    background:radial-gradient(circle at 50% 55%,var(--orange-light) 0%,var(--orange) 45%,var(--orange-deep) 100%);
  }
  .rays{position:absolute;inset:0}
  .header{
    position:absolute;left:0;top:0;width:786px;height:146px;background:var(--white);
    border-bottom-right-radius:40px;
  }
  .brand{
    position:absolute;left:28px;top:18px;display:flex;align-items:center;gap:14px;
  }
  .brand-square{width:52px;height:52px;background:var(--orange);border-radius:6px}
  .brand-name{
    font-size:52px;font-weight:800;color:var(--ink);line-height:1;letter-spacing:1px;
  }
  .brand-kana{
    position:absolute;left:96px;top:84px;font-size:22px;font-weight:800;color:var(--ink);letter-spacing:4px;
  }
  .floor-badge{
    position:absolute;left:536px;top:12px;width:232px;height:280px;
    background:var(--white);border:8px solid var(--orange);border-radius:26px;
    box-shadow:0 0 0 6px var(--white);
    text-align:center;color:var(--orange);font-weight:900;
  }
  .floor-badge .building{font-size:60px;line-height:1;margin-top:16px;letter-spacing:2px}
  .floor-badge .floor{display:flex;justify-content:center;align-items:flex-end;line-height:1;margin-top:4px}
  .floor-badge .num{font-size:180px;line-height:.9}
  .floor-badge .kai{font-size:62px;margin-bottom:8px}
  .tagline{
    position:absolute;left:38px;top:186px;color:var(--white);font-weight:800;
    font-size:29px;line-height:1.5;letter-spacing:0;
  }
  .main-panel{
    position:absolute;left:66px;top:306px;width:654px;height:760px;
    background:var(--white);border:10px solid var(--orange-deep);border-radius:54px;
  }
  .main-panel::before{
    content:"";position:absolute;inset:10px;border:4px solid var(--orange-pale);border-radius:42px;
  }
  .headline{
    position:absolute;left:0;right:0;text-align:center;
    font-size:280px;font-weight:900;line-height:1;color:var(--orange);
    -webkit-text-stroke:14px var(--orange-deep);paint-order:stroke fill;
    letter-spacing:0;
  }
  .headline.line-1{top:46px}
  .headline.line-2{top:380px}
  .skyline{
    position:absolute;left:0;bottom:0;width:786px;height:140px;
  }
</style>
</head>
<body>
<div class="signboard">
  <svg class="rays" viewBox="0 0 786 1200" aria-hidden="true">
    <g fill="#ffffff" opacity="0.08">
      <polygon points="393,660 0,200 0,320"/>
      <polygon points="393,660 0,480 0,600"/>
      <polygon points="393,660 0,760 0,880"/>
      <polygon points="393,660 0,1040 0,1160"/>
      <polygon points="393,660 786,200 786,320"/>
      <polygon points="393,660 786,480 786,600"/>
      <polygon points="393,660 786,760 786,880"/>
      <polygon points="393,660 786,1040 786,1160"/>
    </g>
  </svg>

  <header class="header">
    <div class="brand">
      <span class="brand-square"></span>
      <span class="brand-name">Sunny Nest</span>
    </div>
    <div class="brand-kana">サニーネスト</div>
  </header>

  <div class="floor-badge">
    <div class="building">当ビル</div>
    <div class="floor"><span class="num">5</span><span class="kai">階</span></div>
  </div>

  <p class="tagline">賃貸アパート・マンションなら<br>サニーネストへ!!</p>

  <section class="main-panel">
    <h1 class="headline line-1">賃貸</h1>
    <h1 class="headline line-2">専門</h1>
  </section>

  <div class="skyline" role="img" aria-label="街並みのビルと家のシルエット"
       style="background:linear-gradient(to top,#ffc46b 0%,#ffb347 60%,rgba(255,179,71,0) 100%)"></div>
</div>
</body>
</html>
```